Heritage Hollow Business Cards

Require a business card design. <br/><br/>Needs to include logo (either round or long version) plus these details:<br/>Maya Torvel<br/>Heritage Hollow<br/>maya@quonbrook.com.au<br/>02 6481 7390<br/>PO Box Glenwarra NSW 2913<br/>www.heritagehollow.com.au<br/><br/>I need in an editable format so that I can create for multiple staff members. <br/><br/>

Target Market(s)

We are an online store selling renovation products to home owners are builders. Looking for a classic classy design.

Industry/Entity Type

Home And Garden

Contact Information for Business Card

Maya Torvel
Heritage Hollow
maya@quonbrook.com.au
02 6481 7390
PO Box Glenwarra NSW 2913
www.heritagehollow.com.au

Colors

Designer to choose colors to be used in the design.

Requirements
Must have
• Must include Logo.

```html
<!DOCTYPE html>
<html lang="en">
<head>
<meta charset="utf-8">
<title>Heritage Hollow Business Cards</title>
<link href="https://fonts.googleapis.com/css2?family=Andika:wght@400;700&family=EB+Garamond:wght@500&family=Open+Sans:wght@400&display=swap" rel="stylesheet">
<style>
  :root {
    --bg: #f4f4f2;
    --card-white: #ffffff;
    --brand-green: #4b7564;
    --text-green: #3f6b56;
    --band-green: #a9bdb3;
    --plant-tone: #dfe8e2;
    --ink: #1f1f1f;
    --logo-ink: #2b2b2b;
    --line-white: #f1f5f2;
  }
  * { box-sizing: border-box; margin: 0; padding: 0; }
  html, body { width: 1200px; height: 873px; overflow: hidden; }
  body { background: var(--bg); position: relative; font-family: "Open Sans", sans-serif; }

  .card {
    position: absolute;
    width: 520px;
    height: 317px;
    top: 190px;
    border-radius: 3px;
    box-shadow: 0 10px 28px rgba(0,0,0,.14);
    overflow: hidden;
  }

  /* Front */
  .card-front { left: 50px; background: var(--card-white); }
  .card-front .band {
    position: absolute; left: 0; right: 0; bottom: 0; height: 52px;
    background: linear-gradient(90deg, var(--band-green), #c7d6ce);
    border-top: 2px solid var(--text-green);
  }
  .card-front .plant {
    position: absolute; left: 26px; bottom: 54px; width: 110px; height: 112px;
    background: radial-gradient(ellipse at 50% 40%, var(--plant-tone), rgba(223,232,226,.2));
    border-radius: 6px;
  }
  .card-front .details {
    position: absolute; left: 165px; top: 36px; right: 20px;
  }
  .company-name {
    font-family: "Andika", sans-serif; font-weight: 700;
    color: var(--text-green); font-size: 29px; line-height: 1.1;
  }
  .person-name {
    font-family: "EB Garamond", serif; font-weight: 500;
    color: var(--ink); font-size: 25px; letter-spacing: 1.5px;
    text-transform: uppercase; margin: 14px 0 10px;
  }
  .contact { list-style: none; color: var(--ink); font-size: 15.5px; line-height: 1.5; }

  /* Back */
  .card-back {
    left: 630px; background: var(--brand-green);
    display: flex; align-items: center; justify-content: center;
  }
  .back-mark {
    width: 150px; height: 150px; border: 1.5px solid var(--line-white); border-radius: 50%;
    display: flex; align-items: center; justify-content: center; text-align: center;
    font-family: "Andika", sans-serif; font-weight: 700; font-size: 22px; line-height: 1.1;
    color: var(--line-white);
  }

  /* Standalone wordmark */
  .wordmark {
    position: absolute; right: 80px; bottom: 120px;
    display: flex; align-items: center; gap: 16px;
    font-family: "Andika", sans-serif; font-weight: 700; font-size: 44px;
    color: var(--logo-ink);
  }
  .wordmark .dot {
    width: 22px; height: 22px; border: 2px solid var(--logo-ink); border-radius: 50%;
  }
</style>
</head>
<body>
  <section class="card card-front">
    <div class="plant" role="img" aria-label="Line drawing of a potted leafy plant"></div>
    <div class="details">
      <p class="company-name">Heritage Hollow</p>
      <p class="person-name">Maya Torvel</p>
      <ul class="contact">
        <li>(02) 6481 7390</li>
        <li>maya@quonbrook.com.au</li>
        <li>www.heritagehollow.com.au</li>
        <li>PO Box Glenwarra NSW 2913</li>
      </ul>
    </div>
    <div class="band" role="img" aria-label="Hand-hatched green stripe pattern along the card edge"></div>
  </section>

  <section class="card card-back">
    <div class="back-mark">Heritage<br>Hollow</div>
  </section>

  <div class="wordmark">
    <span class="dot"></span>
    <span>Heritage Hollow</span>
  </div>
</body>
</html>
```